Private practice for psychiatry and psychotherapy needs a business card and logo

I need a logo and business card design for my private practice for psychiatry and psychotherapy. The optional names for my practice are: Vornhoute Praktijk voor Psychiatrie en Psychotherapie, or short: Praktijk Vornhoute.
I am a (child and adolescent) psychiatrist and psychotherapist. I diagnose and treat infants, children, adolescents and adults with psychiatric symptoms/disorders. I also give supervision to colleagues about their own treatments. My work is characterised by personal involvement, transparence, creativity and professionality.
I would like to have an appealing, light and bright, yet basic design that invites people (both children and adults) to contact me, gives trust and hope, without loosing professional appearance.
I uploaded my contact information which should not necessarily be all included (in this form) on the card as long as people know how to contact me. Please feel free to be creative!
Please note that my website is only temporarely and need a new design and update too!

Target Market(s)

Clients and patients (children, adolescents, adults) with psychiatric symptoms who need diagnosis and treatment. I work with private clients and patients through medical insurances.

Industry/Entity Type

Mental Health

Contact Information for Business Card

Dr. Sanne Vornhoute-ter Kuilen
Psychiater/Kinder- en Jeugdpsychiater
Wouter Heskampstraat 14
3071 PX Rotterdam
t: 06-51928764
e: info@praktijkvornhoute.nl
i: www.praktijkvornhoute.nl

Logo Text

Praktijk Vornhoute voor Psychiatrie en Psychotherapie; or short: Praktijk Vornhoute

Font styles to use
Sans Serif
Other font styles liked:
• up to designer

Requirements
Must have
• Appealing, light, bright, creative, trustful, professional and unique.

```html
<!DOCTYPE html>
<html lang="nl">
<head>
<meta charset="utf-8">
<title>Praktijk Vornhoute – visitekaartjes</title>
<link href="https://fonts.googleapis.com/css2?family=Open+Sans:wght@300;400;700&display=swap" rel="stylesheet">
<style>
  :root {
    --backdrop: #d9d9d9;
    --paper: #f4f4f3;
    --ink: #2a2a2a;
    --ink-soft: #4a4a4a;
    --brand-red: #d42a5a;
    --brand-blue: #4d80bd;
  }
  * { margin: 0; padding: 0; box-sizing: border-box; }
  html, body {
    width: 1200px; height: 903px; overflow: hidden;
    background: var(--backdrop);
    font-family: "Open Sans", sans-serif;
    color: var(--ink);
  }
  .sheet {
    position: relative; width: 1200px; height: 903px;
    display: flex; justify-content: center; align-items: center; gap: 96px;
  }
  .card {
    position: relative; width: 362px; height: 560px;
    background: var(--paper);
    box-shadow: 0 2px 4px rgba(0,0,0,.12);
    overflow: hidden;
  }

  /* front */
  .brand-mark {
    position: absolute; top: 120px; left: 0; right: 0;
    display: flex; justify-content: center; align-items: center; gap: 14px;
  }
  .brand-mark__dot { width: 46px; height: 46px; border-radius: 50%; background: var(--brand-blue); }
  .brand-mark__name { font-size: 30px; font-weight: 400; color: var(--brand-red); }
  .practice-name {
    position: absolute; top: 268px; left: 40px; right: 32px; text-align: right;
  }
  .practice-name__title { font-size: 27px; font-weight: 400; letter-spacing: .5px; line-height: 1.1; }
  .practice-name__sub { font-size: 11.5px; font-weight: 400; letter-spacing: .3px; margin-top: 2px; }
  .services {
    position: absolute; bottom: 56px; right: 72px; text-align: right;
    list-style: none; font-size: 15px; font-weight: 300; line-height: 1.18; color: var(--ink-soft);
  }

  /* back */
  .back-mark {
    position: absolute; top: 0; left: 0; right: 0; height: 250px;
    display: flex; justify-content: center; align-items: center; gap: 16px;
  }
  .back-mark__dot { width: 70px; height: 70px; border-radius: 50%; background: var(--brand-blue); }
  .back-mark__name { font-size: 32px; font-weight: 400; color: var(--brand-red); }
  .contact { position: absolute; top: 316px; right: 34px; text-align: right; }
  .contact__name { font-size: 13px; font-weight: 700; color: var(--brand-red); text-transform: uppercase; }
  .contact__role { font-size: 10.5px; font-weight: 700; text-transform: uppercase; }
  .contact__block { font-size: 14px; font-weight: 300; line-height: 1.22; color: var(--ink-soft); margin-top: 36px; margin-right: 50px; }
  .contact__block--web { margin-top: 46px; margin-right: 30px; }
</style>
</head>
<body>
<main class="sheet">
  <section class="card card--front">
    <div class="brand-mark">
      <span class="brand-mark__dot"></span>
      <span class="brand-mark__name">Vornhoute</span>
    </div>
    <div class="practice-name">
      <h1 class="practice-name__title">PRAKTIJK VORNHOUTE</h1>
      <p class="practice-name__sub">VOOR PSYCHIATRIE EN PSYCHOTHERAPIE</p>
    </div>
    <ul class="services">
      <li>PSYCHIATRIE</li>
      <li>PSYCHOTHERAPIE</li>
      <li>LEERTHERAPIE</li>
      <li>SUPERVISIE</li>
    </ul>
  </section>

  <section class="card card--back">
    <div class="back-mark">
      <span class="back-mark__dot"></span>
      <span class="back-mark__name">Vornhoute</span>
    </div>
    <div class="contact">
      <p class="contact__name">Dr. Sanne Vornhoute-ter Kuilen</p>
      <p class="contact__role">Psychiater/Kinder- en Jeugdpsychiater</p>
      <p class="contact__block">Wouter Heskampstraat 14<br>3071 PX Rotterdam<br>06-51928764</p>
      <p class="contact__block contact__block--web">info@praktijkvornhoute.nl<br>www.praktijkvornhoute.nl</p>
    </div>
  </section>
</main>
</body>
</html>
```